Book cover The seven quiet ledgers

I need a book cover for a 6 x 9 inches book.

I prefer white background with clean lines. Bleed is 0.125 inches and spine is 0.27024

The back of the cover must consider the space for the ISBN barcode: 2" wide and 1.2" tall. The bottom of this ISBN barcode is located 1/4" up from the bottom trim line of the cover. The right side of the ISBN barcode is located 1/4" to the left of the spine.

Front cover should have title and subtitle plus author's name. The book is in Spanish so:

title: Las siete rutinas del desvelo
subtitle: Abra las puertas de su calma interior
author: Marta Quiroga Benning

the information about the book is here www.thesevenquietledgers.com

the back cover should have three blocks of information, a summary of the book, testimonials and about the author with a picture (leave space for a picture) Also, there should be a note with our website and bulk purchases

This is the information on the back. No need to add what is in parenthesis.

(about author) Marta Quiroga Benning es una de las expertas internacionales en creación de riqueza. Ha formado ocho empresas y una fundación, incluyendo el primer fondo de inversiones de capital semilla en Chile. Reconocida autora y expositora, ha recorrido el mundo varias veces presentando su sistema Brovanta®

Top (summary)
La mayoría de las personas no estan satisfechas con su prosperidad. Prueban estoy y aquello, hacen cursos, leen libros y mientras todos dicen lo que hay que hacer, nadie explica lo que NO hay que hacer. Si ud. Está estancado, este libro es para ud.

Testimonios (Testimonial):
Un libro que llega al alma. Tomás Verdún.
No solo es importante saber que hacer, sino estar alerta a lo que no debemos hacer. Derek Holloman.
El sistema para cambiar hábitos es excelente. Fernando Ubaldo-ruiz
Nos permite remendar esos pequeños detalles que afectan nuestra autoestima. Margaret Pruitt
Una manera sana de acumular y manejar la prosperidad que nos merecemos. Doreen Blick
Nos recuerda como nuestra percepción subconsciente del dinero afecta nuestro éxito financiero Renata Vail.

Ventas al mayor mpelorin@brovanta-mail.com
www.thesevenquietledgers.com

Target Market(s)

Individuals who feel they are working hard but are not getting the results they want regarding their financial well being.

this is NOT a book to get out of debt or to get rich quick.

this is a book for people who are serious about their lives and feel that, although they are working hard, they are stuck.

the summary of the book in English is found here: www.thesevenquietledgers.com
I am also changing working on the third edition of the book in English, so I wouldn't be using the same cover. you can see the book for sale on Librovia. "The Seven Quiet Ledgers"

Requirements
Must have
• Clean lines, white background, elegant, professional but human.
Nice to have
• an image that represents breaking a habit or getting unstuck. I thought about an anchor or a weigh or car brakes.
Should not have
• Bright colors, faces, pictures

```html
<!DOCTYPE html>
<html lang="es">
<head>
<meta charset="utf-8">
<title>Las siete rutinas del desvelo — cubierta</title>
<link rel="stylesheet" href="https://fonts.googleapis.com/css2?family=Open+Sans:wdth,wght@75..100,300..600&display=swap">
<style>
  :root{
    --page-bg:#eceeec;
    --paper:#ffffff;
    --forest:#4f6b60;
    --forest-dark:#3f5a50;
    --sage:#dfe7da;
    --ink:#5b635f;
    --ink-soft:#7c847f;
    --rule:#d4d9d5;
    --photo-a:#b9a89c;
    --photo-b:#8f7d74;
  }
  *{box-sizing:border-box;margin:0;padding:0}
  html,body{width:1200px;height:900px;overflow:hidden}
  body{background:var(--page-bg);font-family:"Open Sans",Arial,sans-serif;color:var(--ink);position:relative}

  .cover-wrap{position:absolute;left:48px;top:45px;width:1104px;height:810px;display:flex;background:var(--paper);box-shadow:0 0 0 1px var(--rule)}

  /* back cover */
  .back-cover{width:540px;height:100%;display:flex;flex-direction:column;padding-top:40px}
  .back-summary{padding:0 40px 0 44px;font-size:12.5px;line-height:1.6;color:var(--ink)}
  .testimonials{margin-top:24px;background:var(--sage);padding:18px 40px 18px 44px}
  .testimonials h3{font-weight:600;font-size:12px;letter-spacing:.08em;text-transform:uppercase;color:var(--forest);margin-bottom:8px}
  .testimonial{font-size:11.5px;line-height:1.45;margin-bottom:5px;color:var(--ink)}
  .testimonial:last-child{margin-bottom:0}
  .testimonial cite{font-style:normal;color:var(--forest)}
  .author-block{margin-top:26px;padding:0 40px 0 44px;display:flex;gap:20px}
  .author-photo{flex:0 0 118px;height:132px;background:linear-gradient(160deg,var(--photo-a),var(--photo-b))}
  .author-bio{font-size:12px;line-height:1.6;color:var(--ink)}
  .sales-note{margin-top:28px;padding-left:44px;font-size:11.5px;line-height:1.6;color:var(--ink-soft)}
  .sales-note strong{font-weight:600;color:var(--forest)}

  /* spine */
  .spine{width:24px;height:100%;border-left:1px solid var(--rule);border-right:1px solid var(--rule);position:relative;overflow:hidden}
  .spine-text{position:absolute;left:50%;top:50%;transform:translate(-50%,-50%) rotate(90deg);white-space:nowrap;font-size:10.5px;letter-spacing:.06em;color:var(--forest);display:flex;gap:60px;text-transform:uppercase}

  /* front cover */
  .front-cover{width:540px;height:100%;position:relative}
  .front-author{position:absolute;right:42px;top:34px;font-size:15px;color:var(--ink-soft);letter-spacing:.02em}
  .front-title{position:absolute;left:0;right:0;top:118px;text-align:right;font-weight:300;font-stretch:75%;text-transform:uppercase}
  .title-line{display:block;font-size:64px;line-height:1.02;color:var(--forest-dark);padding-right:42px;letter-spacing:.01em}
  .title-band{display:block;margin-top:10px;margin-left:90px;background:var(--forest);padding:4px 0 6px}
  .title-band .title-line{color:#fff}
  .subtitle-band{display:block;margin-left:90px;background:var(--sage);padding:8px 42px 9px 0;font-size:19px;font-stretch:100%;text-transform:none;color:var(--forest-dark)}
</style>
</head>
<body>
  <div class="cover-wrap">
    <section class="back-cover">
      <p class="back-summary">La mayoría de las personas no están satisfechas con su prosperidad. Prueban esto y aquello, hacen cursos, leen libros y mientras todos dicen lo que hay que hacer, nadie explica lo que NO hay que hacer. Si ud. está estancado, este libro es para ud.</p>

      <div class="testimonials">
        <h3>Testimonios</h3>
        <p class="testimonial">Un libro que llega al alma. <cite>Tomás Verdún</cite></p>
        <p class="testimonial">No solo es importante saber qué hacer, sino estar alerta a lo que no debemos hacer. <cite>Derek Holloman</cite></p>
        <p class="testimonial">El sistema para cambiar hábitos es excelente. <cite>Fernando Ubaldo-ruiz</cite></p>
        <p class="testimonial">Nos permite remendar esos pequeños detalles que afectan nuestra autoestima. <cite>Margaret Pruitt</cite></p>
        <p class="testimonial">Una manera sana de acumular y manejar la prosperidad que nos merecemos. <cite>Doreen Blick</cite></p>
        <p class="testimonial">Nos recuerda cómo nuestra percepción subconsciente del dinero afecta nuestro éxito financiero. <cite>Renata Vail</cite></p>
      </div>

      <div class="author-block">
        <div class="author-photo" role="img" aria-label="Retrato de la autora"></div>
        <p class="author-bio">Marta Quiroga Benning es una de las expertas internacionales en creación de riqueza. Ha formado ocho empresas y una fundación, incluyendo el primer fondo de inversiones de capital semilla en Chile. Reconocida autora y expositora, ha recorrido el mundo varias veces presentando su sistema Brovanta®</p>
      </div>

      <p class="sales-note"><strong>Ventas al mayor</strong> mpelorin@brovanta-mail.com<br>www.thesevenquietledgers.com</p>
    </section>

    <section class="spine">
      <div class="spine-text"><span>Las siete rutinas del desvelo</span><span>Marta Quiroga Benning</span></div>
    </section>

    <section class="front-cover">
      <p class="front-author">Marta Quiroga Benning</p>
      <h1 class="front-title">
        <span class="title-line">Las siete</span>
        <span class="title-line">rutinas del</span>
        <span class="title-band"><span class="title-line">desvelo</span></span>
        <span class="subtitle-band">Abra las puertas de su calma interior</span>
      </h1>
    </section>
  </div>
</body>
</html>
```